Corvell Bookkeeping Services business cards

looking for a double sided business card design. My logo is attached. I am looking for a design similar to the attached. Keen to see what my logo in white on the blue background would look like.

```html
<!DOCTYPE html>
<html lang="en">
<head>
<meta charset="UTF-8">
<title>Corvell Bookkeeping Services – Business Cards</title>
<link href="https://fonts.googleapis.com/css2?family=Poppins:wght@400;500;700;800&display=swap" rel="stylesheet">
<style>
  :root {
    --backdrop: #bdbdbd;
    --green: #8fb52c;
    --green-deep: #5e8a3c;
    --navy: #0a3270;
    --navy-deep: #052a66;
    --ink: #2b2b2b;
    --paper: #ffffff;
    --faint: #f0f0f0;
  }
  * { box-sizing: border-box; margin: 0; padding: 0; }
  html, body { width: 1200px; height: 900px; overflow: hidden; }
  body {
    background: var(--backdrop);
    font-family: "Poppins", sans-serif;
    position: relative;
  }
  .card {
    position: absolute;
    width: 600px;
    height: 340px;
    border-radius: 26px;
    overflow: hidden;
    box-shadow: 0 6px 14px rgba(0,0,0,0.25);
  }

  /* Front */
  .card-front {
    left: 70px; top: 80px;
    background: linear-gradient(200deg, var(--green) 0%, var(--green-deep) 38%, #245a62 62%, var(--navy-deep) 100%);
  }
  .card-front .decor-circle {
    position: absolute;
    right: -60px; top: -40px;
    width: 300px; height: 300px;
    border-radius: 50%;
    background: rgba(255,255,255,0.06);
  }
  .wordmark {
    position: absolute;
    display: flex;
    align-items: center;
    gap: 14px;
    font-weight: 700;
  }
  .wordmark .mark-square {
    width: 46px; height: 46px;
    border-radius: 6px;
  }
  .wordmark .name { font-size: 64px; line-height: 1; letter-spacing: -1px; }
  .wordmark .sub { font-size: 15px; letter-spacing: 2.4px; text-transform: uppercase; margin-top: 4px; }
  .card-front .wordmark { left: 140px; top: 118px; color: var(--paper); }
  .card-front .mark-square { background: var(--paper); }

  /* Back */
  .card-back {
    left: 530px; top: 480px;
    background: var(--paper);
  }
  .card-back .decor-circle {
    position: absolute;
    right: -40px; top: -70px;
    width: 320px; height: 320px;
    border-radius: 50%;
    background: var(--faint);
  }
  .card-back .wordmark { left: 70px; top: 42px; color: var(--navy); }
  .card-back .wordmark .name { font-size: 56px; }
  .card-back .wordmark .sub { font-size: 13px; }
  .card-back .mark-square { background: var(--navy); width: 40px; height: 40px; }

  .person { position: absolute; left: 80px; top: 166px; }
  .person-name { font-size: 26px; font-weight: 700; line-height: 1.1; }
  .person-name .first { color: var(--green); }
  .person-name .last { color: var(--navy); }
  .person-title { font-size: 16px; color: var(--ink); }
  .accent-block {
    position: absolute; left: 40px; top: 172px;
    width: 22px; height: 44px; background: var(--green);
  }

  .contacts { position: absolute; left: 80px; top: 238px; list-style: none; }
  .contacts li {
    display: flex; align-items: center; gap: 10px;
    font-size: 16px; color: var(--ink); line-height: 26px;
  }
  .contacts svg { width: 16px; height: 16px; flex: none; }
  .contacts .highlight { color: var(--green); }

  .address {
    position: absolute; right: 36px; top: 178px;
    text-align: right; font-size: 15px; color: var(--ink); line-height: 1.35;
  }

  .band-green {
    position: absolute; left: 0; bottom: 0;
    width: 380px; height: 12px; background: var(--green);
  }
  .band-navy {
    position: absolute; left: 386px; right: 0; bottom: 0;
    height: 22px; background: var(--navy);
  }
</style>
</head>
<body>

<section class="card card-front" aria-label="Front of business card">
  <div class="decor-circle"></div>
  <div class="wordmark">
    <div class="mark-square"></div>
    <div>
      <div class="name">Corvell</div>
      <div class="sub">Bookkeeping Services</div>
    </div>
  </div>
</section>

<section class="card card-back" aria-label="Back of business card">
  <div class="decor-circle"></div>
  <div class="wordmark">
    <div class="mark-square"></div>
    <div>
      <div class="name">Corvell</div>
      <div class="sub">Bookkeeping Services</div>
    </div>
  </div>

  <div class="accent-block"></div>
  <div class="person">
    <div class="person-name"><span class="first">Martin</span> <span class="last">Hale</span></div>
    <div class="person-title">Managing Director</div>
  </div>

  <ul class="contacts">
    <li>
      <svg viewBox="0 0 24 24" fill="var(--navy)"><path d="M6.6 10.8a15.1 15.1 0 0 0 6.6 6.6l2.2-2.2c.3-.3.7-.4 1-.2 1.1.4 2.3.6 3.6.6.6 0 1 .4 1 1V20c0 .6-.4 1-1 1A17 17 0 0 1 3 4c0-.6.4-1 1-1h3.5c.6 0 1 .4 1 1 0 1.3.2 2.5.6 3.6.1.3 0 .7-.2 1z"/></svg>
      044-987 654 321
    </li>
    <li>
      <svg viewBox="0 0 24 24" fill="var(--navy)"><path d="M2 5h20v14H2z M2 5l10 8 10-8" stroke="var(--paper)" stroke-width="1.5"/></svg>
      info@corvellbooks.com
    </li>
    <li>
      <svg viewBox="0 0 24 24" fill="none" stroke="var(--navy)" stroke-width="2"><circle cx="12" cy="12" r="9"/><path d="M3 12h18M12 3c3 3.5 3 14.5 0 18M12 3c-3 3.5-3 14.5 0 18"/></svg>
      <span>www.<span class="highlight">corvellbooks</span>.com</span>
    </li>
  </ul>

  <div class="address">
    87, Harrow Lane, Suite 4<br>
    73918, Eastmere
  </div>

  <div class="band-green"></div>
  <div class="band-navy"></div>
</section>

</body>
</html>
```